Book cover for book about Climate Change

Looking for a clean, bold, and attractive cover for a mass-market paperback (5.5"x 8.5") about solving the climate change problem. Title is either "When Rivers Learn to Sing” or A Lantern Over Quiet Fields” (your choice), subtitle is "A five-step plan to reverse climate change — to ensure that your grandchildren will live on a clean and comfortable planet," author is Dale Pruitt. Thinking that it *might* feature an image of Earth (or a portion thereof) and its very thin layer of atmosphere -- but STRONGLY encourage other ideas too!

Requirements
Nice to have
• Keep it positive — NOT scary doom-and-gloom

```html
<!DOCTYPE html>
<html lang="en">
<head>
<meta charset="utf-8">
<title>A Lantern Over Quiet Fields — Book Cover</title>
<link href="https://fonts.googleapis.com/css2?family=Bebas+Neue&family=Montserrat:wght@400;500&family=Oswald:wght@500&display=swap" rel="stylesheet">
<style>
  :root {
    --backdrop: #f0c6bd;
    --sky-top: #2c4f58;
    --sky-mid: #6b8f95;
    --horizon: #8aa9ad;
    --water-deep: #34616a;
    --water-low: #1f3f47;
    --title-gold: #f6b93f;
    --paper-white: #eef4f4;
  }
  * { margin: 0; padding: 0; box-sizing: border-box; }
  html, body {
    width: 1200px;
    height: 880px;
    overflow: hidden;
    background: var(--backdrop);
  }
  .canvas {
    position: relative;
    width: 1200px;
    height: 880px;
  }
  .book-cover {
    position: absolute;
    left: 340px;
    top: 38px;
    width: 520px;
    height: 804px;
    overflow: hidden;
    box-shadow: 0 18px 40px rgba(80, 40, 35, 0.18);
  }
  .cover-art {
    position: absolute;
    inset: 0;
    width: 100%;
    height: 100%;
    display: block;
  }
  .title {
    position: absolute;
    top: 34px;
    right: 26px;
    text-align: right;
    font-family: "Bebas Neue", "Oswald", sans-serif;
    font-weight: 400;
    font-size: 92px;
    line-height: 0.86;
    letter-spacing: 1px;
    color: var(--title-gold);
  }
  .subtitle {
    position: absolute;
    top: 468px;
    left: 40px;
    right: 40px;
    text-align: center;
    font-family: "Montserrat", sans-serif;
    font-weight: 400;
    font-size: 14px;
    line-height: 1.35;
    color: var(--paper-white);
  }
  .author {
    position: absolute;
    left: 34px;
    bottom: 50px;
    font-family: "Oswald", sans-serif;
    font-weight: 500;
    font-size: 20px;
    letter-spacing: 2px;
    color: var(--paper-white);
  }
</style>
</head>
<body>
  <main class="canvas">
    <article class="book-cover">
      <svg class="cover-art" viewBox="0 0 520 804" preserveAspectRatio="none" role="img" aria-label="Photograph of planet Earth half submerged in calm sea water under a grey-teal sky">
        <defs>
          <linearGradient id="skyWater" x1="0" y1="0" x2="0" y2="1">
            <stop offset="0" stop-color="var(--sky-top)"/>
            <stop offset="0.3" stop-color="var(--sky-mid)"/>
            <stop offset="0.5" stop-color="var(--horizon)"/>
            <stop offset="0.52" stop-color="var(--water-deep)"/>
            <stop offset="1" stop-color="var(--water-low)"/>
          </linearGradient>
          <radialGradient id="globeGlow" cx="0.68" cy="0.5" r="0.38">
            <stop offset="0" stop-color="#b9cfd2" stop-opacity="0.55"/>
            <stop offset="1" stop-color="#b9cfd2" stop-opacity="0"/>
          </radialGradient>
        </defs>
        <rect width="520" height="804" fill="url(#skyWater)"/>
        <rect width="520" height="804" fill="url(#globeGlow)"/>
      </svg>

      <h1 class="title">A Lantern<br>Over Quiet<br>Fields</h1>

      <p class="subtitle">A five-step plan to reverse climate change to ensure that your grandchildren will live on a clean and comfortable planet.</p>

      <p class="author">DALE PRUITT</p>
    </article>
  </main>
</body>
</html>
```